Business Cards and Stationary Package
TallyCrest Partners, LLC
Use same font as used in my logo
Designer Discretion
Professional
Marcy T. Welling
President
418 Kestrel Lane
Harbor Pines, FL 32199
mwelling@tallycrest-partners.com
www.tallycrest-partners.com
Please be creative, yet professional and simple.

```html
<!DOCTYPE html>
<html lang="en">
<head>
<meta charset="utf-8">
<title>TallyCrest Partners, LLC – Business Card</title>
<link rel="stylesheet" href="https://fonts.googleapis.com/css2?family=Cinzel:wght@600&family=Tinos&display=swap">
<style>
  :root {
    --stage: #ecebe8;
    --paper: #ffffff;
    --brand-blue: #1f47a8;
    --brand-blue-deep: #0d3c9b;
    --brand-green: #4a9a1c;
    --brand-green-light: #6cbf2a;
    --sky-light: #1aa3e6;
    --sky-dark: #0a5cc0;
    --ink-grey: #555555;
    --white: #ffffff;
  }
  * { box-sizing: border-box; margin: 0; padding: 0; }
  html, body { width: 1200px; height: 720px; overflow: hidden; }
  body { background: var(--stage); position: relative; font-family: "Tinos", "Times New Roman", serif; }

  .card {
    position: absolute;
    top: 212px;
    width: 520px;
    height: 297px;
    overflow: hidden;
    box-shadow: 0 6px 18px rgba(0,0,0,.18);
  }
  .card--front { left: 60px; background: var(--paper); }
  .card--back  { left: 620px; background: radial-gradient(circle at 45% 45%, var(--sky-light) 0%, var(--sky-dark) 85%); }

  .card__art { position: absolute; inset: 0; width: 100%; height: 100%; }

  .brand {
    position: absolute;
    left: 30px;
    top: 74px;
    font-family: "Cinzel", "Times New Roman", serif;
    font-weight: 600;
    font-size: 17px;
    color: var(--brand-blue);
    letter-spacing: .5px;
    white-space: nowrap;
  }

  .holder { position: absolute; left: 30px; top: 172px; }
  .holder__name {
    font-family: "Cinzel", "Times New Roman", serif;
    font-weight: 600; font-size: 17px;
    color: var(--brand-blue);
  }
  .holder__title {
    font-family: "Cinzel", "Times New Roman", serif;
    font-weight: 600; font-size: 11px;
    color: var(--brand-green); letter-spacing: .5px;
  }
  .holder__address {
    margin-top: 12px;
    font-size: 12.5px; line-height: 1.3;
    color: var(--ink-grey);
  }

  .contact {
    position: absolute; right: 20px; top: 84px;
    list-style: none; text-align: right;
    color: var(--white); font-size: 12.5px; line-height: 1.55;
  }
  .contact li { display: flex; align-items: center; justify-content: flex-end; gap: 6px; white-space: nowrap; }
  .contact svg { width: 10px; height: 10px; fill: var(--white); }
  .contact__gap { height: 18px; }

  .back__name {
    position: absolute; left: 0; right: 0; top: 128px;
    text-align: center;
    font-family: "Cinzel", "Times New Roman", serif;
    font-weight: 600; font-size: 30px;
    color: var(--white); letter-spacing: 1px;
  }
  .back__web {
    position: absolute; left: 0; right: 0; bottom: 34px;
    text-align: center; color: var(--white);
    font-size: 13px; letter-spacing: 3px;
  }
</style>
</head>
<body>

<section class="card card--front" aria-label="Business card front">
  <svg class="card__art" viewBox="0 0 520 297" preserveAspectRatio="none" aria-hidden="true">
    <defs>
      <linearGradient id="green-swoosh" x1="0" y1="0" x2="1" y2="1">
        <stop offset="0" stop-color="var(--brand-green)"/>
        <stop offset="1" stop-color="var(--brand-green-light)"/>
      </linearGradient>
    </defs>
    <path d="M318 0 C350 110 320 220 190 297 L520 297 L520 0 Z" fill="var(--brand-blue-deep)"/>
    <path d="M334 0 C368 110 336 220 206 297 L520 297 L520 0 Z" fill="url(#green-swoosh)"/>
    <path d="M400 0 C440 20 470 60 520 66 L520 0 Z" fill="var(--brand-blue-deep)"/>
  </svg>

  <p class="brand">TallyCrest Partners, LLC</p>

  <div class="holder">
    <p class="holder__name">Marcy T. Welling</p>
    <p class="holder__title">President</p>
    <p class="holder__address">418 Kestrel Lane<br>Harbor Pines, FL 32199</p>
  </div>

  <ul class="contact">
    <li><svg viewBox="0 0 10 10"><path d="M2 0h2l1 3-1.5 1a6 6 0 0 0 2.5 2.5L7 5l3 1v2c0 1-1 2-2 2A8 8 0 0 1 0 2c0-1 1-2 2-2z"/></svg>555-310-4826</li>
    <li><svg viewBox="0 0 10 10"><path d="M1 4h8v5H1zM3 1h4v3H3z"/></svg>555-310-7193</li>
    <li>www.tallycrest-partners.com</li>
    <li class="contact__gap"></li>
    <li><svg viewBox="0 0 10 10"><circle cx="5" cy="5" r="5"/></svg>www.tallycrest-partners.com</li>
    <li><svg viewBox="0 0 10 10"><path d="M0 2h10v6H0z"/></svg>mwelling@tallycrest-partners.com</li>
  </ul>
</section>

<section class="card card--back" aria-label="Business card back">
  <p class="back__name">TallyCrest Partners</p>
  <p class="back__web">www.tallycrest-partners.com</p>
</section>

</body>
</html>
```